Home Design company focused on remodel and enhancement of kitchens and bathroorms

I already have a logo designed by ArtHarbor, I now need a design for my business cards.
The company is in the remodeling and enhancement industry for homes, focusing on kitchens and bathrooms, however, we can remodel or enhance every room in a home, an office space, etc.

The company's name is VELMOR HOME DESIGN, LLC

We'll focus on clients in the Rio Grande Valley, Texas. Primarily McAllen, Edinburg, Pharr, Mission, Brownsville and South Padre Island.

The design on the business card should transmit reliability, professionalism anda bit of upscale design.

The logo is in black and white, and would like to keep it that way.

The information that needs to be printed in the business cards is:
Company's name: Velmor Home Design
Company's Logo (attached)
My name: Noel Bramwit
Address, phone and email:
2715 N Parkline Road, Ste 348
McAllen, TX 78501
(956) 555 0187
nbramwit@velmordesign.example
Website: velmordesign.example

```html
<!DOCTYPE html>
<html lang="en">
<head>
<meta charset="UTF-8">
<title>Velmor Home Design – Business Card</title>
<link rel="stylesheet" href="https://fonts.googleapis.com/css2?family=Montserrat:wght@400;500;600;700&display=swap">
<style>
  :root {
    --ink: #000000;
    --paper: #ffffff;
    --card-border: #3a3a3a;
  }
  * { margin: 0; padding: 0; box-sizing: border-box; }
  html, body {
    width: 1200px;
    height: 1000px;
    overflow: hidden;
    background: var(--paper);
    font-family: "Montserrat", sans-serif;
    color: var(--ink);
  }
  .card {
    position: absolute;
    left: 198px;
    width: 804px;
    height: 460px;
  }
  .card--front {
    top: 16px;
    background: var(--ink);
  }
  .card--back {
    top: 525px;
    background: var(--paper);
    border: 1px solid var(--card-border);
  }
  .brand {
    position: absolute;
    display: flex;
    align-items: center;
    gap: 18px;
    font-weight: 500;
    letter-spacing: 0.2em;
    text-transform: uppercase;
  }
  .brand__mark {
    flex: none;
  }
  .brand__name {
    display: flex;
    flex-direction: column;
  }
  .card--front .brand {
    left: 256px;
    top: 198px;
    color: var(--paper);
    font-size: 21px;
    line-height: 24px;
  }
  .card--front .brand__mark {
    width: 58px;
    height: 58px;
    background: var(--paper);
  }
  .card--back .brand {
    left: 59px;
    top: 202px;
    color: var(--ink);
    font-size: 18px;
    line-height: 20px;
  }
  .card--back .brand__mark {
    width: 50px;
    height: 50px;
    background: var(--ink);
  }
  .person {
    position: absolute;
    left: 415px;
    top: 70px;
  }
  .person__name {
    font-size: 24px;
    font-weight: 700;
    line-height: 30px;
  }
  .person__role {
    margin-top: 12px;
    font-size: 18px;
    font-weight: 600;
  }
  .contact {
    position: absolute;
    left: 415px;
    top: 221px;
    font-size: 18.5px;
    line-height: 26px;
    list-style: none;
  }
  .contact__row {
    display: flex;
    margin-bottom: 10px;
  }
  .contact__row--address { margin-top: 2px; line-height: 31px; }
  .contact__label {
    width: 35px;
    flex: none;
  }
</style>
</head>
<body>
  <section class="card card--front">
    <div class="brand">
      <span class="brand__mark"></span>
      <span class="brand__name"><span>Velmor</span><span>Home</span><span>Design</span></span>
    </div>
  </section>

  <section class="card card--back">
    <div class="brand">
      <span class="brand__mark"></span>
      <span class="brand__name"><span>Velmor</span><span>Home</span><span>Design</span></span>
    </div>

    <div class="person">
      <h1 class="person__name">Noel Bramwit</h1>
      <p class="person__role">CEO</p>
    </div>

    <ul class="contact">
      <li class="contact__row"><span class="contact__label">p:</span><span>(956) 555 0187</span></li>
      <li class="contact__row"><span class="contact__label">e:</span><span>nbramwit@velmordesign.example</span></li>
      <li class="contact__row"><span class="contact__label">w:</span><span>velmordesign.example</span></li>
      <li class="contact__row contact__row--address"><span class="contact__label">a:</span><span>2715 N Parkline Road, Ste 348<br>McAllen, TX 78501</span></li>
    </ul>
  </section>
</body>
</html>
```